Give us a remarkable appearance

We need a unique, remarkable stationery design (Business Cards, Business Letters, Email Signature etc.). The design should use our logo.

Veltro-Consulting is a startup in consulting, management and IT services and individual software development for the financial industry.

Veltro in english is agate stone. We would like to see designs that use colors out of the agate stone color range.

Preferred COLORS: gold, dark red (burgundy), white, dark grey, black ** see attached Logos **

The used font should be available for further usage with texts etc.

The design should express: modernity, precious, high quality, lightness, stability, ecological awareness, speedy, reliability, simplicity, sustainability.

Target Market(s)

C-Level and Business Clients, Professionals

Industry/Entity Type

Business

Logo Text

Logo styles of interest
Pictorial/Combination Logo
Abstract Logo
Wordmark Logo
Requirements
Must have
• Business Cards, Business Papers, Email Signature
Nice to have
• Door plate, Flyersheet (basic structure), Envelop...

```html
<!DOCTYPE html>
<html lang="en">
<head>
<meta charset="utf-8">
<title>Veltro Consulting – Stationery</title>
<link rel="stylesheet" href="https://fonts.googleapis.com/css2?family=Montserrat:wght@600;700&family=Arimo:wght@400;700&display=swap">
<style>
  :root{
    --backdrop:#d9d9d9;
    --backdrop-light:#ececec;
    --paper:#ffffff;
    --gold:#d9ae17;
    --band:#eac51a;
    --ink:#1a1a1a;
    --body-ink:#2b2b2b;
  }
  *{margin:0;padding:0;box-sizing:border-box;}
  html,body{width:1200px;height:1200px;overflow:hidden;}
  body{
    position:relative;
    background:radial-gradient(circle at 50% 50%,var(--backdrop-light) 0%,var(--backdrop) 75%);
    font-family:"Arimo",Arial,sans-serif;
    color:var(--ink);
  }
  .sheet{
    position:absolute;top:262px;width:481px;height:676px;
    background:var(--paper);
    box-shadow:0 1px 4px rgba(0,0,0,.12);
  }
  .cover{left:84px;}
  .letter{left:637px;}

  .brand{
    position:absolute;display:flex;align-items:center;
    font-family:"Montserrat",sans-serif;font-weight:600;color:var(--gold);
    line-height:1;letter-spacing:0;white-space:nowrap;
  }
  .brand-mark{display:block;background:var(--gold);flex:none;}

  .cover .brand{left:46px;top:306px;font-size:36px;gap:14px;}
  .cover .brand-mark{width:30px;height:30px;}

  .letter .brand{left:32px;top:32px;font-size:17px;gap:8px;}
  .letter .brand-mark{width:15px;height:15px;}

  .web-band{
    position:absolute;left:37px;top:628px;width:407px;height:29px;
    background:var(--band);
    display:flex;align-items:center;justify-content:center;
    font-family:"Montserrat",sans-serif;font-weight:700;font-size:15px;letter-spacing:1px;color:var(--ink);
  }

  .letter-body{position:absolute;left:43px;top:108px;width:395px;}
  .salutation{font-size:9.5px;margin-bottom:13px;color:var(--body-ink);}
  .letter-body p{font-size:7.1px;line-height:11.6px;color:var(--body-ink);margin-bottom:12px;}
  .letter-body p.joined{margin-bottom:0;}

  .contact{position:absolute;top:624px;left:0;right:0;display:flex;justify-content:flex-end;padding-right:34px;
    font-family:"Montserrat",sans-serif;font-weight:700;font-size:7.6px;line-height:10.5px;color:var(--ink);white-space:nowrap;}
  .contact-address{text-align:right;padding-right:7px;border-right:1px solid var(--ink);}
  .contact-lines{padding-left:7px;}
</style>
</head>
<body>
  <section class="sheet cover">
    <div class="brand"><span class="brand-mark"></span>Veltro Consulting</div>
    <div class="web-band">WWW.VELTROCONSULTING.COM</div>
  </section>

  <section class="sheet letter">
    <div class="brand"><span class="brand-mark"></span>Veltro Consulting</div>
    <div class="letter-body">
      <div class="salutation">Dear Name,</div>
      <p>Lorem ipsum dolor sit amet, consectetur adipiscing elit. Proin lorem ipsum, tempus id adipiscing eu, vulputate eget dui. Aliquam eget nibh sem, a gravida mauris. Vestibulum lorem magna, dictum eu adipiscing sed, congue vitae odio. Duis vel volutpat dui. Etiam eu semper orci. Proin nisi est, sodales sit amet mollis at, mattis accumsan metus. Nullam cursus neque eget mauris accumsan vitae sodales mauris vehicula. Ut interdum, erat eget facilisis pulvinar, orci diam dignissim felis, et lacinia dolor est vitae elit. Aenean justo purus, feugiat vitae consectetur sed, molestie a purus. Cras pretium mauris sed nunc pharetra vitae convallis magna vestibulum.</p>
      <p>Nunc facilisis, est in luctus accumsan, erat magna faucibus eros, in faucibus ante lorem sed velit. Fusce vehicula lectus id turpis ornare vitae lacinia dolor eleifend. Aliquam enim odio, fermentum sed vehicula vel, pellentesque id mauris. Pellentesque quam risus, faucibus ac congue sit amet, posuere non lorem. Cras interdum volutpat nisl et tincidunt. Aliquam feugiat erat consequat turpis tincidunt adipiscing. In lacus ipsum, condimentum rhoncus congue in, pharetra ac magna. Pellentesque habitant morbi tristique senectus et netus et malesuada fames ac turpis ege.</p>
      <p class="joined">Nunc varius, sapien sed sodales sollicitudin, lorem tellus semper mi, vel viverra purus ante sit amet ligula. Vestibulum ornare lectus vel eros rhoncus eget euismod ipsum euismod. Praesent molestie auctor eros non viverra.</p>
      <p>Aliquam vehicula hendrerit orci, ut ornare ante aliquam eget. Phasellus luctus justo ullamcorper elit porttitor dignissim. Proin et sem ac mauris euismod suscipit. Morbi rutrum, urna non posuere ullamcorper, neque libero eleifend sem, eu tincidunt nibh lectus ac elit. Proin eget pretium nulla. Donec dolor lectus, tristique quis semper at, aliquam a leo. Nunc purus nisl, imperdiet ut tempor ut, luctus porttitor quam. Morbi facilisis vestibulum neque et varius. Praesent sit amet nisl tellus. Praesent ut mi sed lacus commodo lobortis non ac lectus. Aenean condimentum porttitor tempus. Etiam mauris diam, eleifend et scelerisque et, venenatis a dui. Proin eros purus, placerat ac adipiscing sed, dignissim vitae orci. Nunc porta nisl ac leo blandit ultrices. In congue commodo turpis, quis auctor lacus dictum vitae.</p>
      <p>Cras semper libero sit amet sapien convallis et tristique urna ultrices. In ornare hendrerit erat sed varius. Quisque aliquet, lorem eu ultricies interdum, tortor justo convallis risus, at eleifend dui tellus eu erat. Duis lacinia libero vitae metus fringilla mattis. Donec lacinia, ligula at ultricies sollicitudin, risus ligula vulputate tortor, at vestibulum arcu ipsum vitae leo elementum aliquet faucibus.</p>
    </div>
    <div class="contact">
      <div class="contact-address">14 ORCHARD ROW, SUITE 2<br>LAKEVIEW, 000000<br>T : 0000 555 0142</div>
      <div class="contact-lines">F : 0000 555 0187<br>E : INFO@VELTROCONSULTING.COM<br>W : WWW.VELTROCONSULTING.COM</div>
    </div>
  </section>
</body>
</html>
```